Foldable Flyer Din A4 Charging Infrastructure Real Estate

We need a flyer (size Din A4, folded, see image).
Attached you will find the content with a rough arrangement.
The inner part will contain some Q&A, we have sketched two possible arrangements of the content.
We are looking for a professional design and a good, clean layout.
Maybe you have some ideas how to arrange the content in a smarter way, we are open for suggestions.
The draft contains no images. It would be good to have an explaining image at least on the front of the flyer.
Attached you will find some stock photos we are using on our website, but you can also propose your own images.
If useful, here is our webpage:
https://strom-nest.de/
and the landing page for the offering
https://strom-nest. en/charging-solutions-for-house-management-and-routes/
(this landing page is not professionally designed, so feel free to create a better design for the flyer)
Our target group are real estate managers/facility managers of larger apartment buildings.
The offering is: full-serviced solutions for charging infrastructure for electric cars at the parking lots for residents.
Please do not hesitate to contact me, if you need further information.
Target Market(s)
Professionals in real estate management, facility management
Industry/Entity Type
charging infrastructures for electric cars, focus: appartment buildings
Look and feel
Each slider illustrates characteristics of the customer's brand and the style your logo design should communicate.

```html
<!DOCTYPE html>
<html lang="de">
<head>
<meta charset="utf-8">
<title>strom-nest.de – Faltflyer Ladeinfrastruktur</title>
<link href="https://fonts.googleapis.com/css2?family=Exo+2:wght@400;500;600&family=Poppins:wght@400;500;600;700&display=swap" rel="stylesheet">
<style>
:root{
  --navy:#141a29;
  --purple:#7b5ea7;
  --magenta:#d63a8f;
  --pink-text:#c2307e;
  --lilac:#efe9f6;
  --lilac-line:#b99bd6;
  --white:#ffffff;
  --ink:#1f2230;
}
*{box-sizing:border-box;margin:0;padding:0}
html,body{width:1200px;height:2458px;overflow:hidden;background:var(--white)}
body{position:relative;font-family:"Poppins",sans-serif;color:var(--ink)}
.panel{position:absolute;left:455px;width:223px;overflow:hidden}
.photo{position:absolute;left:0;right:0}
.head{font-family:"Exo 2",sans-serif}
.pill{position:absolute;left:50%;transform:translateX(-50%);height:19px;border-radius:10px;
  background:linear-gradient(90deg,var(--purple),var(--magenta));color:var(--white);
  font-family:"Exo 2",sans-serif;font-weight:600;font-size:12px;letter-spacing:.5px;
  display:flex;align-items:center;justify-content:center;white-space:nowrap}
.wordmark{font-family:"Poppins",sans-serif;font-weight:600;color:var(--navy);display:flex;align-items:center;gap:6px}
.wordmark .dot{width:12px;height:12px;border-radius:50%;background:var(--magenta)}
svg.curve{position:absolute;left:0;width:100%}

/* cover */
.cover{top:0;height:475px;background:var(--white)}
.cover .wordmark{position:absolute;top:52px;left:0;right:0;justify-content:center;font-size:19px}
.cover .photo{top:100px;height:252px;border-top-left-radius:40px;
  background:linear-gradient(135deg,#8c8fb8 0%,#4b4f7a 45%,#2c3158 70%,#6e6a8c 100%)}
.cover .dark{position:absolute;top:340px;left:0;right:0;bottom:0;background:var(--navy)}
.cover .title{position:absolute;top:374px;left:0;right:0;text-align:center;color:var(--white);font-size:14px;line-height:15px;letter-spacing:.3px}
.cover .sub{position:absolute;top:416px;left:0;right:0;text-align:center;color:var(--white);font-size:14px;letter-spacing:.3px}

/* intro */
.intro{top:487px;height:473px;background:var(--white)}
.intro .photo{top:0;height:150px;background:linear-gradient(120deg,#b9a7c6 0%,#e6dcea 45%,#9a8aa8 100%)}
.intro h2{position:absolute;top:178px;left:14px;right:10px;font-size:10.5px;line-height:13px;font-weight:600}
.checks{position:absolute;top:226px;left:14px;list-style:none;font-size:10.5px;line-height:16px}
.checks li{display:flex;align-items:center;gap:5px}
.tick{width:10px;height:10px;border:1px solid var(--magenta);border-radius:50%;display:inline-flex;align-items:center;justify-content:center}
.feature{position:absolute;left:14px;right:8px;display:flex;gap:9px;font-size:8px;line-height:10.5px}
.ico{flex:0 0 25px;height:25px;border-radius:4px;background:linear-gradient(135deg,var(--purple),var(--magenta));display:flex;align-items:center;justify-content:center}
.ico i{width:11px;height:11px;border:1.5px solid var(--white);border-radius:50%}

/* q&a */
.qa{top:970px;width:447px;height:465px;background:var(--white)}
.qa .photo{top:0;height:118px;background:linear-gradient(180deg,#b6b6c2 0%,#7c7f8f 50%,#3a3d4a 100%)}
.qa .cols{position:absolute;top:140px;font-family:"Exo 2",sans-serif;font-weight:500;font-size:11px}
.row{position:absolute;left:13px;width:422px;height:46px}
.q{position:absolute;left:0;top:0;width:117px;height:46px;border:1px solid var(--lilac-line);border-radius:5px;background:var(--lilac);
  color:var(--pink-text);font-weight:600;padding:0 17px 0 6px;display:flex;align-items:center;overflow:hidden}
.q span{display:block;font-size:6.4px;line-height:7.4px}
.a{position:absolute;left:126px;top:0;width:296px;height:46px;border:1px solid var(--lilac-line);border-radius:5px;background:var(--lilac);
  padding:0 8px 0 17px;display:flex;align-items:center;overflow:hidden}
.a span{display:block;font-size:6.5px;line-height:7.6px;text-align:justify}
.a b{font-weight:700}
.badge{position:absolute;left:107px;top:8px;width:30px;height:30px;border-radius:50%;border:3px solid var(--white);
  background:linear-gradient(135deg,var(--purple),var(--magenta));box-shadow:0 0 0 1px var(--lilac-line)}
.badge::after{content:"";position:absolute;left:8px;top:6px;width:8px;height:12px;border:1.5px solid var(--white);border-radius:2px}

/* steps */
.steps{top:1455px;height:473px;background:var(--navy)}
.steps h3{position:absolute;top:25px;left:23px;color:var(--magenta);font-size:10.5px;line-height:11.5px;font-weight:600;font-family:"Exo 2",sans-serif}
.timeline{position:absolute;left:34px;top:80px;width:2px;height:150px;background:var(--magenta)}
.step{position:absolute;left:23px;right:8px;display:flex;gap:10px}
.step .ico{flex:0 0 24px;height:24px}
.step h4{color:var(--magenta);font-family:"Exo 2",sans-serif;font-size:10.5px;font-weight:500;line-height:12px}
.step ul{list-style:none;color:var(--white);font-size:6.8px;line-height:8px}
.step li::before{content:"• "}
.steps .photo{top:332px;height:141px;border-top-left-radius:40px;background:linear-gradient(135deg,#d9e6f2 0%,#9fb8d3 50%,#5f7fa8 100%)}

/* back */
.back{top:1943px;height:472px;background:linear-gradient(180deg,var(--purple) 0%,#a356a8 60%,var(--magenta) 100%)}
.back .wordmark{position:absolute;top:52px;left:32px;font-size:15px;color:var(--navy)}
.point{position:absolute;left:12px;right:8px;display:flex;gap:9px;font-size:7.2px;line-height:8.6px;color:var(--white)}
.point .ico{flex:0 0 22px;height:22px;background:var(--navy);border:1px solid var(--white)}
.cta{position:absolute;top:237px;left:13px;width:198px;height:95px;border-radius:10px;background:var(--navy);color:var(--white);text-align:center}
.cta .lead{font-family:"Exo 2",sans-serif;font-size:14px;line-height:16px;margin-top:12px}
.cta .pill{top:51px;width:172px;font-size:13px}
.cta .phone{position:absolute;top:75px;left:0;right:0;font-size:12px;font-weight:500;display:flex;align-items:center;justify-content:center;gap:4px}
.back .dark{position:absolute;top:355px;left:0;right:0;bottom:0;background:var(--navy)}
.imprint{position:absolute;top:372px;left:0;right:0;text-align:center;color:var(--white);font-size:7px;line-height:8.6px}
</style>
</head>
<body>

<section class="panel cover">
  <div class="wordmark"><span class="dot"></span>strom-nest.de</div>
  <svg class="curve" style="top:40px" height="70" viewBox="0 0 223 70"><path d="M0 60 Q8 56 40 56 L185 56 Q215 56 223 10" fill="none" stroke="#7b5ea7" stroke-width="3"/></svg>
  <div class="photo" role="img" aria-label="Foto: Ladekabel steckt an einer Ladesäule in einer beleuchteten Tiefgarage"></div>
  <svg class="curve" style="top:300px" height="60" viewBox="0 0 223 60"><path d="M0 60 L0 50 Q10 42 60 42 L170 42 Q215 42 223 0 L223 60 Z" fill="#141a29"/><path d="M0 50 Q10 42 60 42 L170 42 Q215 42 223 0" fill="none" stroke="#d63a8f" stroke-width="3"/></svg>
  <div class="dark"></div>
  <p class="title head">Flexible Ladeinfrastrukturen<br>für die Elektromobilität</p>
  <p class="sub head">für Mieter und Eigentümer</p>
  <div class="pill" style="top:444px;width:158px">www.strom-nest.de</div>
</section>

<section class="panel intro">
  <div class="photo" role="img" aria-label="Foto: Ladeanschluss eines Elektroautos, im Hintergrund eine Bewohnerin an einer Wallbox"></div>
  <svg class="curve" style="top:100px" height="60" viewBox="0 0 223 60"><path d="M0 60 L0 52 Q8 44 50 44 L180 44 Q218 44 223 0 L223 60 Z" fill="#fff"/><path d="M0 52 Q8 44 50 44 L180 44 Q218 44 223 0" fill="none" stroke="#7b5ea7" stroke-width="3"/></svg>
  <h2>Bieten Sie ihren Bewohnern Lademöglichkeiten für ihre Elektrofahrzeuge –</h2>
  <ul class="checks">
    <li><span class="tick"><svg width="6" height="6" viewBox="0 0 6 6"><path d="M1 3 L2.5 4.5 L5 1.5" fill="none" stroke="#d63a8f" stroke-width="1"/></svg></span>einfach,</li>
    <li><span class="tick"><svg width="6" height="6" viewBox="0 0 6 6"><path d="M1 3 L2.5 4.5 L5 1.5" fill="none" stroke="#d63a8f" stroke-width="1"/></svg></span>unkompliziert und</li>
    <li><span class="tick"><svg width="6" height="6" viewBox="0 0 6 6"><path d="M1 3 L2.5 4.5 L5 1.5" fill="none" stroke="#d63a8f" stroke-width="1"/></svg></span>zukunftsfähig</li>
  </ul>
  <div class="feature" style="top:288px"><span class="ico"><i></i></span><p>Zukunftsfähig durch flexibles Abrechnungsmodell für verschiedene Einsatzmöglichkeiten.</p></div>
  <div class="feature" style="top:329px"><span class="ico"><i></i></span><p>Leichter, schneller Einstieg in das Thema, unkomplizierte und professionelle Abwicklung</p></div>
  <div class="feature" style="top:370px"><span class="ico"><i></i></span><p>Aufbau und Betrieb von Ladelösungen speziell für Hausverwaltungen und WEGs</p></div>
  <div class="pill" style="top:410px;width:158px">www.strom-nest.de</div>
  <svg class="curve" style="top:430px" height="43" viewBox="0 0 223 43"><path d="M0 43 L0 30 Q6 12 40 10 L223 10 L223 43 Z" fill="#141a29"/></svg>
</section>

<section class="panel qa">
  <div class="photo" role="img" aria-label="Foto: dunkles Elektroauto in einer Garage neben einer Wallbox"></div>
  <svg class="curve" style="top:80px" height="60" viewBox="0 0 447 60"><path d="M0 60 L0 40 Q10 36 60 36 L400 36 Q440 36 447 0 L447 60 Z" fill="#fff"/><path d="M0 40 Q10 36 60 36 L400 36 Q440 36 447 0" fill="none" stroke="#7b5ea7" stroke-width="3"/></svg>
  <p class="cols" style="left:20px;color:var(--pink-text)">Problem / Fragestellung</p>
  <p class="cols" style="left:159px;color:var(--purple)">Der Lösungsansatz von strom-nest</p>

  <div class="row" style="top:160px"><p class="q"><span>Ein Bewohner will eine Wallbox – was tun?</span></p><p class="a"><span>Mieter/Eigentümer hat nach WoMoG Anspruch auf eine Wallbox. Die Hausverwaltung darf den Wunsch nicht verhindern, darf aber – und sollte – Vorgaben machen, um eine nachhaltige Gesamtlösung sicherzustellen. <b>strom-nest</b> liefert diese Vorgaben, damit Installation und weiterer Ausbau der Ladeinfrastruktur geordnet erfolgen kann.</span></p><span class="badge"></span></div>
  <div class="row" style="top:211px"><p class="q"><span>Der Stromanschluss reicht nicht, wenn alle Bewohner eine Wallbox wollen!</span></p><p class="a"><span>Mit Hilfe des <b>Last-Managements</b> von <b>strom-nest</b> lässt sich die verfügbare Strom-Kapazität intelligent steuern, so dass der Hausanschluss in der Regel langfristig ausreicht.</span></p><span class="badge"></span></div>
  <div class="row" style="top:262px"><p class="q"><span>Sind die Vorabprüfung und der Einbau von Ladeinfrastruktur teuer? Wie überzeugt man die WEG von den Kosten?</span></p><p class="a"><span>Bei der Lösung von <b>strom-nest</b> werden nur aktuell benötigte Wallboxen aufgebaut <b>– erforderliche Investitionen erfolgen schrittweise nach Bedarf.</b> Mit dem optionalen Mietmodell entstehen der WEG keine oder nur geringe Kosten, hier können die Kosten größtenteils auf die Nutzer der Wallboxen verlagert werden.</span></p><span class="badge"></span></div>
  <div class="row" style="top:313px"><p class="q"><span>Die Bewohner haben keine fest zugeordneten Stellplätze</span></p><p class="a"><span>Der Anschluss an den Wohnungszähler des jeweiligen Mieters/Eigentümers ist nicht notwendig. <b>strom-nest</b> rechnet auf Wunsch mit jedem Mieter direkt dessen Ladestromverbrauch ab.</span></p><span class="badge"></span></div>
  <div class="row" style="top:364px"><p class="q"><span>Wer kann helfen, eine professionelle und zukunftsfähige Ladeinfrastruktur zu entwickeln?</span></p><p class="a"><span><b>strom-nest</b> ist Spezialist für Ladeinfrastruktur, und kennt sich neben der speziellen technischen Lösungen auch mit rechtlichen Fragestellungen und Abrechnungslösungen aus. Neben der Umsetzung unterstützt strom-nest die Hausverwaltungen bei technischen und juristischen Fragen, um zusammen mit der WEG eine optimale Lösung aufzubauen.</span></p><span class="badge"></span></div>
  <div class="row" style="top:415px"><p class="q"><span>Bei uns wurden bereits Wallboxen von einzelnen Mietern installiert, was nun?</span></p><p class="a"><span>In vielen Fällen kann Hardware anderer Hersteller in die Abrechnungslösung von <b>strom-nest</b> integriert werden.</span></p><span class="badge"></span></div>
</section>

<section class="panel steps">
  <h3>Die Schritte zur<br>Ladeinfrastruktur in<br>Ihrem Objekt:</h3>
  <div class="timeline"></div>
  <div class="step" style="top:68px"><span class="ico"><i></i></span><div><h4>Erstprüfung</h4><ul><li>Machbarkeitsprüfung</li><li>Abschätzung, Planung nächster Schritte</li></ul></div></div>
  <div class="step" style="top:113px"><span class="ico"><i></i></span><div><h4>Konzeption</h4><ul><li>Planung der Anlage</li><li>Abstimmung Netzbetreiber</li><li>Kostenkalkulation</li></ul></div></div>
  <div class="step" style="top:162px"><span class="ico"><i></i></span><div><h4>Installation</h4><ul><li>Installation von Verkabelung und<br>&nbsp;&nbsp;Elektrotechnik</li><li>Installation der Wallboxen</li><li>Setup der Abrechnungssysteme</li></ul></div></div>
  <div class="step" style="top:218px"><span class="ico"><i></i></span><div><h4>Betrieb</h4><ul><li>Technischer Betrieb</li><li>Abrechnung</li><li>Regelmäßige Wartung (DGUV3)</li><li>Anmeldung und Verwaltung neuer Nutzer</li></ul></div></div>
  <div class="pill" style="top:279px;width:158px">www.strom-nest.de</div>
  <div class="photo" role="img" aria-label="Foto: Ladestecker an einem hellen Elektroauto mit leuchtendem Anschluss"></div>
  <svg class="curve" style="top:280px" height="70" viewBox="0 0 223 70"><path d="M0 70 L0 62 Q6 46 50 46 L180 46 Q218 46 223 0" fill="none" stroke="#d63a8f" stroke-width="3"/></svg>
</section>

<section class="panel back">
  <div class="wordmark"><span class="dot"></span>strom-nest.de</div>
  <div class="point" style="top:100px"><span class="ico"><i></i></span><p>Hausverwaltungen werden von Mietern und Eigentümern immer öfter konfrontiert mit dem Wunsch nach Lademöglichkeiten für die Bewohner.</p></div>
  <div class="point" style="top:144px"><span class="ico"><i></i></span><p>Zudem verlangt das neue Gebäude-Elektromobilitäts-infrastruktur Gesetz (GEIG) den Ausbau der Ladeinfrastruktur bei der Renovierung der TG.</p></div>
  <div class="point" style="top:188px"><span class="ico"><i></i></span><p>Als Anbieter von Full-Service-Lösungen ermöglicht strom-nest eine für Immobilienbesitzer/-verwalter einfache und ausbaubare Lösung, die alle Bereiche abdeckt.</p></div>
  <div class="cta">
    <p class="lead">Jetzt Beratungsgespräch<br>anfordern unter:</p>
    <div class="pill">www.strom-nest.de/WEG</div>
    <p class="phone">oder <svg width="11" height="11" viewBox="0 0 12 12"><circle cx="6" cy="6" r="5.2" fill="none" stroke="#fff" stroke-width="1"/><path d="M4 3.2 L5 3 L5.6 4.6 L5 5.1 Q5.6 6.5 6.9 7 L7.4 6.4 L9 7 L8.8 8 Q6.5 8.6 4.6 6.6 Q3.3 5 4 3.2Z" fill="#fff"/></svg> 01234 / 567 89 00</p>
  </div>
  <svg class="curve" style="top:345px" height="30" viewBox="0 0 223 30"><path d="M0 30 L0 26 Q8 10 50 10 L223 10 L223 30 Z" fill="#141a29"/><path d="M0 26 Q8 10 50 10 L223 10" fill="none" stroke="#fff" stroke-width="2"/></svg>
  <div class="dark"></div>
  <div class="imprint">
    <p>strom-nest GmbH<br>Lindenweg 14<br>82000 Seefeld</p>
    <p style="margin-top:9px">HRB 100200<br>Amtsgericht München<br>Geschäftsführung: Marta Linden</p>
    <p style="margin-top:9px">Email: info@strom-nest.de<br>Tel.: 01234 / 567 89 00</p>
  </div>
</section>

</body>
</html>
```